Pagecraft website update with basic ecomm features

We need an update to our existing website
www.brightmoorhub.com.au that can be easily updated, enhances our logo and can take payments online and a basic text logo suite for 3 products. Website would reflect confidence and give clients confidence in the outcomes we will provide for them. must be easy to use, crisp, fresh, clean and dynamic.

Target Market(s)

entrepreneurs, professionals, small business owners, corporate organisations, universities

Industry/Entity Type

Online

Coding

Coded - Design and coding required

Number of Pages Required

5+ page

Font styles to use
Sans Serif

Requirements
Must have
• be easy to navigate, look professional, please see brief doc
Nice to have
• please see briefing doc
Should not have
• please see briefing doc

```html
<!DOCTYPE html>
<html lang="en">
<head>
<meta charset="utf-8">
<title>Brightmoor Hub</title>
<link rel="stylesheet" href="https://fonts.googleapis.com/css2?family=Roboto:ital,wght@0,400;0,500;0,700;1,400&display=swap">
<style>
:root{
  --hero-blue:#2f73aa;
  --hero-blue-deep:#1f5e93;
  --hero-blue-light:#5f9cca;
  --band-dark:#4a4a4a;
  --band-mid:#5e5e5e;
  --panel-left:#3b434a;
  --panel-right:#4b555f;
  --ink:#222831;
  --muted:#6d7884;
  --accent:#2d7fc1;
  --strip:#f3f4f6;
  --footer-top:#3a3a3a;
  --footer-bottom:#5a5a5a;
  --white:#ffffff;
  --line:#9aa1a8;
}
*{box-sizing:border-box;margin:0;padding:0}
html,body{width:1200px;height:2659px;overflow:hidden;background:var(--white)}
body{font-family:'Roboto',sans-serif;color:var(--ink);position:relative}
section,header,footer{position:absolute;left:0;width:1200px}
.abs{position:absolute}

/* hero */
.hero{top:0;height:544px;background:linear-gradient(180deg,var(--hero-blue) 0%,var(--hero-blue-deep) 100%);overflow:hidden}
.hero-photo{position:absolute;inset:0;background:linear-gradient(135deg,#3b82b9 0%,#2b6da2 55%,#245e8f 100%)}
.hero-sheen{position:absolute;inset:0}
.brand{position:absolute;left:52px;top:5px;width:160px;text-align:center}
.brand-mark{display:block;width:106px;height:105px;margin:0 auto;background:#0d0d0d;border-radius:6px}
.brand-name{display:block;margin-top:9px;font-size:13px;letter-spacing:2.4px;color:#111;font-weight:400}
.nav{position:absolute;top:24px;left:0;list-style:none}
.nav li{position:absolute;color:var(--white);font-size:14px;font-weight:500;white-space:nowrap;transform:translateX(-50%)}
.auth{position:absolute;top:16px;height:32px;border-radius:16px;font-size:13px;font-weight:500;display:flex;align-items:center;justify-content:center}
.auth.login{left:1008px;width:62px;border:2px solid var(--white);color:var(--white)}
.auth.signup{left:1075px;width:80px;background:var(--white);color:#111}

/* why band */
.why{top:544px;height:112px;background:linear-gradient(90deg,var(--band-dark),var(--band-mid));color:var(--white);text-align:center}
.section-title{font-size:21px;font-weight:700}
.rule{position:absolute;left:55px;width:1092px;border-top:2px dotted var(--line)}
.why .section-title{position:absolute;top:2px;width:100%;line-height:32px}
.why .rule{top:40px;border-color:#cfcfcf}
.why p{position:absolute;top:62px;left:55px;width:1092px;font-size:13px;line-height:19px}

/* products */
.products{top:656px;height:221px}
.products .section-title{position:absolute;top:6px;width:100%;text-align:center;line-height:28px}
.products .rule{top:45px}
.product{position:absolute;top:65px;width:348px;height:124px}
.product-photo{position:absolute;inset:0}
.product-label{position:absolute;left:14px;right:14px;top:103px;height:44px;background:linear-gradient(180deg,#3c3c3c,#5a5a5a);border-radius:4px;color:var(--white);font-size:17px;font-weight:500;display:flex;align-items:center;justify-content:center}

/* about + mail */
.about-mail{top:877px;height:376px}
.about{position:absolute;left:0;top:0;width:600px;height:376px;background:var(--panel-left);color:var(--white);text-align:center}
.about h2,.mail h2{font-size:28px;font-weight:500;position:absolute;top:20px;width:100%}
.about p{position:absolute;left:40px;width:520px;font-size:14.5px;line-height:22px}
.btn-outline{position:absolute;left:243px;top:312px;width:117px;height:38px;border:1.5px solid var(--white);border-radius:4px;font-size:12.5px;font-weight:500;display:flex;align-items:center;justify-content:center;letter-spacing:.4px}
.mail{position:absolute;left:600px;top:0;width:600px;height:376px;background:var(--panel-right);text-align:center;color:var(--white)}
.field{position:absolute;background:var(--white);border-radius:3px;color:#9aa0a6;font-size:11.5px;text-align:left;padding:9px 12px}
.btn-solid{position:absolute;left:233px;top:316px;width:135px;height:32px;background:var(--white);color:#111;border-radius:3px;font-size:12.5px;font-weight:500;display:flex;align-items:center;justify-content:center}
.badge-square{position:absolute;background:var(--white);border-radius:3px;box-shadow:0 2px 6px rgba(0,0,0,.25)}

/* offerings */
.offerings{top:1253px;height:463px;border-bottom:1px solid #e6e8ea}
.offerings .section-title{position:absolute;top:10px;width:100%;text-align:center;line-height:28px}
.offerings .rule{top:51px}
.offer-art{position:absolute;left:51px;top:103px;width:536px;height:337px}
.accordion{position:absolute;left:613px;top:0;width:540px;list-style:none}
.acc-item{position:absolute;left:0;width:540px;height:30px;display:flex;align-items:center}
.acc-icon{width:27px;height:27px;border-radius:4px;display:flex;align-items:center;justify-content:center;margin-right:12px;flex:none}
.acc-item.open .acc-icon{background:#2b2b2b}
.acc-title{font-size:16px;color:#333}
.acc-body{position:absolute;left:39px;top:142px;width:500px;font-size:12.8px;line-height:19px;color:var(--muted)}
.acc-body em{font-style:normal;color:var(--accent)}

/* testimonials */
.testimonials{top:1716px;height:393px}
.testimonials .section-title{position:absolute;top:8px;width:100%;text-align:center;line-height:28px}
.testimonials .rule{top:50px}
.divider-h{position:absolute;left:55px;top:216px;width:1092px;border-top:1.5px dashed #a9aeb3}
.divider-v{position:absolute;left:600px;top:106px;height:234px;border-left:1.5px dashed #a9aeb3}
.quote{position:absolute;width:362px;font-size:12.5px;line-height:19.5px;font-style:italic;color:var(--muted)}
.quote.left{text-align:right}
.author{position:absolute;font-size:12.5px;color:#222}
.author span{color:#1f5fa0}
.author.left{text-align:right;width:362px}
.avatar{position:absolute;width:76px;height:76px;border-radius:50%}

/* partners */
.partners{top:2109px;height:139px;background:var(--strip)}
.partner{position:absolute;top:69px;display:flex;align-items:center;gap:8px;font-size:15px;font-weight:500;color:#3a3a3a;transform:translate(-50%,-50%);white-space:nowrap}
.partner i{display:block;width:24px;height:24px;border-radius:50%;background:#4a4a4a}

/* footer */
.site-footer{top:2248px;height:411px;background:linear-gradient(180deg,var(--footer-top),var(--footer-bottom));color:var(--white)}
.col-title{position:absolute;top:48px;font-size:17.5px;font-weight:500}
.foot-text{position:absolute;font-size:13px;line-height:19.5px}
.foot-text b{font-weight:700}
.map{position:absolute;left:333px;top:88px;width:536px;height:202px}
.socials{position:absolute;left:51px;top:270px;display:flex;gap:12px}
.socials i{display:block;width:14px;height:14px;border-radius:50%;border:2px solid var(--white)}
.foot-rule{position:absolute;left:51px;top:345px;width:1096px;border-top:1px solid #8c8c8c}
.copyright{position:absolute;top:373px;width:100%;text-align:center;font-size:12.5px}
</style>
</head>
<body>

<header class="hero">
  <div class="hero-photo" role="img" aria-label="Photograph of a bright office desk with a laptop, tinted blue, with a faint line chart running across it"></div>
  <svg class="hero-sheen" width="1200" height="544" viewBox="0 0 1200 544" aria-hidden="true">
    <polygon points="0,0 629,0 452,544 0,544" fill="#7fb2d9" opacity=".28"/>
  </svg>
  <div class="brand">
    <span class="brand-mark"></span>
    <span class="brand-name">BRIGHTMOOR HUB</span>
  </div>
  <ul class="nav">
    <li style="left:360px">HOME</li>
    <li style="left:450px">ABOUT US</li>
    <li style="left:558px">WHY US</li>
    <li style="left:665px">SERVICES</li>
    <li style="left:748px">FAQ</li>
    <li style="left:830px">CONTACT</li>
  </ul>
  <div class="auth login">Log In</div>
  <div class="auth signup">Sign Up</div>
</header>

<section class="why">
  <h2 class="section-title">Why Brightmoor Hub</h2>
  <div class="rule"></div>
  <p>Sed ut perspiciatis unde omnis iste natus error sit voluptatem accusantium doloremque laudantium, totam rem aperiam, eaque ipsa quae ab illo inventore veritatis et quasi architecto beatae vitae dicta.</p>
</section>

<section class="products">
  <h2 class="section-title">Our Products</h2>
  <div class="rule"></div>
  <div class="product" style="left:51px">
    <div class="product-photo" role="img" aria-label="Photograph of a glass office hallway with people by the windows" style="background:linear-gradient(135deg,#8aa3b8,#4d6478)"></div>
    <div class="product-label">Product _ 1</div>
  </div>
  <div class="product" style="left:426px">
    <div class="product-photo" role="img" aria-label="Photograph of a man in a light shirt working on a laptop in an office" style="background:linear-gradient(135deg,#d9dde2,#8a96a3)"></div>
    <div class="product-label">Product _ 2</div>
  </div>
  <div class="product" style="left:801px">
    <div class="product-photo" role="img" aria-label="Photograph of a desk with documents and a calculator in a teal tint" style="background:linear-gradient(135deg,#3fb3a6,#1f8e85)"></div>
    <div class="product-label">Product _ 3</div>
  </div>
</section>

<section class="about-mail">
  <div class="about">
    <h2>About Us</h2>
    <p style="top:89px">Sed ut perspiciatis unde omnis iste natus error sit voluptatem accusantium doloremque laudantium, totam rem aperiam, eaque ipsa quae ab illo inventore veritatis et quasi architecto beatae vitae dicta sunt explicabo. Nemo enim ipsam voluptatem quia voluptas.</p>
    <p style="top:201px">Sed ut perspiciatis unde omnis iste natus error sit voluptatem accusantium doloremque laudantium, totam rem aperiam, eaque ipsa quae ab illo inventore veritatis et quasi architecto beatae vitae dicta sunt explicabo. Nemo enim ipsam voluptatem quia voluptas.</p>
    <div class="btn-outline">LEARN MORE</div>
  </div>
  <div class="mail">
    <h2>Feel Free to Mail</h2>
    <div class="field" style="left:50px;top:78px;width:240px;height:31px">Name *</div>
    <div class="field" style="left:309px;top:78px;width:241px;height:31px">Email *</div>
    <div class="field" style="left:50px;top:130px;width:500px;height:32px">Subject</div>
    <div class="field" style="left:50px;top:181px;width:500px;height:114px">Write Your Message Here...</div>
    <div class="btn-solid">SEND MESSAGE</div>
  </div>
  <div class="badge-square" style="left:567px;top:148px;width:68px;height:69px"></div>
</section>

<section class="offerings">
  <h2 class="section-title">About our offerings</h2>
  <div class="rule"></div>
  <div class="offer-art" role="img" aria-label="Grey illustration of a presenter at an easel chart with an audience seated around a table" style="background:linear-gradient(180deg,#f0f0f0 0%,#d6d6d6 100%)"></div>
  <ul class="accordion">
    <li class="acc-item open" style="top:108px">
      <span class="acc-icon"><svg width="12" height="8" viewBox="0 0 12 8"><path d="M1 7 L6 2 L11 7" fill="none" stroke="#fff" stroke-width="2"/></svg></span>
      <span class="acc-title">Outline of program</span>
    </li>
    <li class="acc-body">Opinion polls are an integral part of political debates, the state of the economy, social trends and more. Simply put, we report what people think, along with what they do, because it is important. We generate <em>original</em> public opinion data and other information that is relevant, timely and accurate</li>
    <li class="acc-item" style="top:242px">
      <span class="acc-icon"><svg width="10" height="7" viewBox="0 0 10 7"><path d="M1 1 L5 5 L9 1" fill="none" stroke="#555" stroke-width="1.5"/></svg></span>
      <span class="acc-title">What we deliver</span>
    </li>
    <li class="acc-item" style="top:299px">
      <span class="acc-icon"><svg width="10" height="7" viewBox="0 0 10 7"><path d="M1 1 L5 5 L9 1" fill="none" stroke="#555" stroke-width="1.5"/></svg></span>
      <span class="acc-title">Outcomes</span>
    </li>
    <li class="acc-item" style="top:356px">
      <span class="acc-icon"><svg width="10" height="7" viewBox="0 0 10 7"><path d="M1 1 L5 5 L9 1" fill="none" stroke="#555" stroke-width="1.5"/></svg></span>
      <span class="acc-title">What comes after the program</span>
    </li>
    <li class="acc-item" style="top:411px">
      <span class="acc-icon"><svg width="10" height="7" viewBox="0 0 10 7"><path d="M1 1 L5 5 L9 1" fill="none" stroke="#555" stroke-width="1.5"/></svg></span>
      <span class="acc-title">How the modules are structured? Agenda</span>
    </li>
  </ul>
</section>

<section class="testimonials">
  <h2 class="section-title">What People Say</h2>
  <div class="rule"></div>
  <div class="divider-h"></div>
  <div class="divider-v"></div>

  <p class="quote left" style="left:101px;top:108px">At vero eos et accusamus et iusto odio dignissimos ducimus qui blanditiis praesentium voluptatum deleniti atque corrupti quos dolores et quas molestias excepturi sint occaecati.</p>
  <p class="author left" style="left:101px;top:178px">Owen Halberg , <span>Developer</span></p>
  <div class="avatar" role="img" aria-label="Portrait photo of a client" style="left:491px;top:110px;background:#cdb8a6"></div>

  <div class="avatar" role="img" aria-label="Portrait photo of a client" style="left:633px;top:110px;background:#b49884"></div>
  <p class="quote" style="left:739px;top:108px;width:405px">Luis aute irure dolor in reprehenderit in piluptate velit esse cillum dolore eu fugiat nulla pariatur. Excepteur sint occaecat cupidatat non proident, sunt in culpa qui officia deserunt mollit.</p>
  <p class="author" style="left:739px;top:178px">Priya Castell , <span>Manager</span></p>

  <p class="quote left" style="left:101px;top:242px">Provident, similique sunt in culpa qui officia deserunt mollitia animi, id est laborum et dolorum fuga. Et harum quidem rerum facilis est et expedita distinctio. Nam libero tempore, cum soluta nobis.</p>
  <p class="author left" style="left:101px;top:314px">Nora Whitlow , <span>Creative Designer</span></p>
  <div class="avatar" role="img" aria-label="Portrait photo of a client" style="left:491px;top:248px;background:#8a7466"></div>

  <div class="avatar" role="img" aria-label="Portrait photo of a client" style="left:633px;top:248px;background:#9a8372"></div>
  <p class="quote" style="left:739px;top:242px;width:405px">Duis aute irure dolor in reprehenderit in voluptate velit esse cillum dolore eu fugiat nulla pariatur. Excepteur sint occaecat cupidatat non proident, sunt in culpa qui officia deserunt mollit.</p>
  <p class="author" style="left:739px;top:314px">Reuben Ashby , <span>Operations Manager</span></p>
</section>

<section class="partners">
  <div class="partner" style="left:128px"><i></i>Postwing</div>
  <div class="partner" style="left:322px"><i></i>Pagecraft</div>
  <div class="partner" style="left:503px"><i></i>Postwing</div>
  <div class="partner" style="left:699px"><i></i>Pagecraft</div>
  <div class="partner" style="left:882px"><i></i>Postwing</div>
  <div class="partner" style="left:1072px"><i></i>Pagecraft</div>
  <div class="badge-square" style="left:1069px;top:107px;width:71px;height:68px"></div>
</section>

<footer class="site-footer">
  <h3 class="col-title" style="left:51px">Contact Us</h3>
  <p class="foot-text" style="left:51px;top:88px;width:250px">Maecenas etos sit amet, consectetur adipiscing elit. Terminal volutpat rutrum metro amet sollicitudin interdum.</p>
  <p class="foot-text" style="left:51px;top:164px"><b>Phone:</b> +1 (800) 555 01 24</p>
  <p class="foot-text" style="left:51px;top:198px"><b>Office:</b> 1742 Alder Lane, Portland</p>
  <p class="foot-text" style="left:51px;top:232px"><b>Email:</b> hello@brightmoorhub.com.au</p>
  <div class="socials"><i></i><i></i><i></i><i></i><i></i></div>

  <h3 class="col-title" style="left:546px">Latest Twitts</h3>
  <div class="map" role="img" aria-label="Street map of a city waterfront with a location pin" style="background:linear-gradient(135deg,#e9e4d6 0%,#cfe3c4 45%,#9ec7e6 100%)"></div>

  <h3 class="col-title" style="left:895px">About Team</h3>
  <p class="foot-text" style="left:895px;top:88px;width:252px">Enim congue blandit. Lorem ipsum dolor sit amet, consectetur adipiscing elit. Quisque consectetur interdum finibus. Vestibulum ante ipsum primis in faucibus orci. luctus et ultrices posuere.</p>
  <p class="foot-text" style="left:895px;top:198px;width:252px">Cubilia cras blandit finibus ipsum, id porttitor arcu volutpat a. Integer iaculis erat nec justo malesuada faucibus vel tempus sapien. Vivamus aliquam euismod tristique.</p>

  <div class="foot-rule"></div>
  <p class="copyright">Copyright 2020. All Rights Reserved by Company Name</p>
</footer>

</body>
</html>
```